Business Cards for new orthopaedic surgery practice

My husband and I are starting our own orthopaedic surgery practice. We are looking for a business card that is uniform, but one will have my name/title and the other will have his. You can just create one design with my name on it for now. But when I choose your design as the winning design I will ask that you add another copy with his name/title.

We are looking for classy, simple, elite all in one. We like dark blues/a little gold/yellow. Something that goes with our logo. We want our logo incorporated. Here is all the info you need:
Business name: RV Spine & Vitality Center
Location: 38157 North Harbor Blvd
Coral Springs, FL 33058
Phone: 954-218-4630
Fax: 954-581-2473
Email: info@myrvspine.example

Names: Lorena Vickers, M.D.
Board Certified Hand and Upper Extremity Surgeon

Eban Sorley, M.D.
Board Certified Hip & Knee Replacement/General Orthopaedic Surgeon

Can decide what you want to put on the back. Maybe a slogan:
Rooted in Care. Focused on You

I am just going to upload our logo. The only thing is if we select you as the winning design, the location, and phone numbers may change. We will need your help to update that once fully solidified.

Industry/Entity Type

Medical

Contact Information for Business Card

Colors
0054AA
0677BA
7BADD7
CADEEF
E8F1F8
0094D4
00A9DD
6FCCEA
C7EBF8
E9F6FB

Requirements
Must have
• class, appeal,
Should not have
• We want to air on the side of masculine if we are looking at masculine vs. feminine feel. But we still want it classy, sophisticated, and something we will love

```html
<!DOCTYPE html>
<html lang="en">
<head>
<meta charset="utf-8">
<title>RV Spine &amp; Vitality Center – Business Cards</title>
<link href="https://fonts.googleapis.com/css2?family=Marcellus&family=Noto+Serif:wght@400&display=swap" rel="stylesheet">
<style>
  :root {
    --navy: #233a83;
    --cyan: #1bb3e3;
    --paper: #fcfcfd;
    --backdrop: #1d1c21;
  }
  * { margin: 0; padding: 0; box-sizing: border-box; }
  html, body { width: 720px; height: 1200px; overflow: hidden; background: var(--backdrop); }
  .canvas {
    width: 720px; height: 1200px;
    display: flex; flex-direction: column; align-items: center; justify-content: center; gap: 37px;
  }
  .card {
    position: relative; width: 492px; height: 246px;
    background: var(--paper); border-radius: 14px; overflow: hidden;
    box-shadow: 0 4px 14px rgba(0,0,0,.45);
  }
  .card__band {
    position: absolute; left: 0; right: 0; bottom: 0; height: 49px;
    background: var(--navy);
    display: flex; align-items: center;
  }
  .band-text {
    font-family: "Noto Serif", serif; color: var(--cyan);
    text-transform: uppercase; letter-spacing: 4px; font-size: 10.5px;
    white-space: nowrap;
  }

  /* Front */
  .front__brand {
    position: absolute; top: 0; left: 0; right: 0; height: 197px;
    display: flex; align-items: center; justify-content: center; gap: 12px;
  }
  .brand-dot { width: 16px; height: 16px; border-radius: 50%; background: var(--cyan); flex: none; }
  .front__name {
    font-family: "Marcellus", serif; color: var(--navy);
    font-size: 25px; line-height: 1;
  }
  .front .card__band { justify-content: center; }
  .front .band-text { letter-spacing: 5.5px; font-size: 11.5px; }

  /* Back */
  .back__brand {
    position: absolute; left: 18px; top: 48px;
    display: flex; align-items: center; gap: 10px;
  }
  .back__name {
    font-family: "Marcellus", serif; color: var(--navy);
    font-size: 17px; line-height: 1.05;
  }
  .back__address {
    position: absolute; left: 22px; top: 134px;
    font-family: "Noto Serif", serif; color: var(--navy);
    font-size: 12.5px; line-height: 16px;
  }
  .physicians { position: absolute; left: 233px; top: 20px; width: 252px; }
  .physician { margin-bottom: 10px; }
  .physician__name {
    font-family: "Marcellus", serif; color: var(--cyan);
    font-size: 15.5px; line-height: 17px; text-transform: uppercase; letter-spacing: .3px;
  }
  .physician__title {
    font-family: "Noto Serif", serif; color: var(--navy);
    font-size: 11.5px; line-height: 14.5px; white-space: nowrap;
  }
  .contact { position: absolute; left: 233px; top: 145px; list-style: none; }
  .contact li {
    display: flex; align-items: center; gap: 7px;
    font-family: "Noto Serif", serif; color: var(--navy);
    font-size: 11.5px; line-height: 15px;
  }
  .contact svg { width: 10px; height: 10px; fill: var(--cyan); flex: none; }
  .back .card__band { padding: 0 22px 0 22px; gap: 0; }
  .back .band-text { font-size: 8px; letter-spacing: 1.9px; }
  .band-text--left { width: 211px; }
</style>
</head>
<body>
<main class="canvas">
  <section class="card front" aria-label="Card front">
    <div class="front__brand">
      <span class="brand-dot"></span>
      <span class="front__name">RV Spine &amp; Vitality Center</span>
    </div>
    <div class="card__band"><span class="band-text">Rooted in care. Focused on you</span></div>
  </section>

  <section class="card back" aria-label="Card back">
    <div class="back__brand">
      <span class="brand-dot"></span>
      <span class="back__name">RV Spine &amp;<br>Vitality Center</span>
    </div>
    <p class="back__address">38157 North Harbor Blvd, Suite 5<br>Coral Springs, FL 33058</p>

    <div class="physicians">
      <div class="physician">
        <h2 class="physician__name">Lorena Vickers, M.D.</h2>
        <p class="physician__title">Board Certified Hand<br>and Upper Extremity Surgeon</p>
      </div>
      <div class="physician">
        <h2 class="physician__name">Eban Sorley, M.D.</h2>
        <p class="physician__title">Board Certified Hip &amp; Knee Replacement/<br>General Orthopedic Surgeon</p>
      </div>
    </div>

    <ul class="contact">
      <li><svg viewBox="0 0 10 10" aria-hidden="true"><path d="M1 3.5C1 2 2.5 1 5 1s4 1 4 2.5L7.5 4.3 6.8 3H3.2L2.5 4.3zM2.5 5h5L9 9H1z"/></svg>954-218-4630</li>
      <li><svg viewBox="0 0 10 10" aria-hidden="true"><path d="M2.5 0h5v3h-5zM0 3.5h10v4H8V6H2v1.5H0zM2.5 6.5h5V10h-5z"/></svg>954-581-2473</li>
      <li><svg viewBox="0 0 10 10" aria-hidden="true"><path d="M0 2h10L5 5.5zM0 3.2l5 3.5 5-3.5V8.5H0z"/></svg>info@myrvspine.example</li>
    </ul>

    <div class="card__band">
      <span class="band-text band-text--left">www.lvickershand.example</span>
      <span class="band-text">www.sorleyhipandknee.example</span>
    </div>
  </section>
</main>
</body>
</html>
```